New business card design
Brovalco Upkeep LLC
Project: New business card design
New business card design -
Creative Brief
Professional
Darrel Wickham
President & CEO
2847 Tallow Bend Rd Norristown PA 19403
wwwdw@brovalco-example.com
www.brovalco-example.com
* Professionally done for less than the rest * Commercial & Residential;Interior & Exterior Window washing/Cleaning, Green House,Skylight,Gutter,Power washing services,Customized cleaning programs,Fully licensed, insured, and bonded professionals.

```html
<!DOCTYPE html>
<html lang="en">
<head>
<meta charset="utf-8">
<title>Brovalco Upkeep LLC – Business Card</title>
<link rel="stylesheet" href="https://fonts.googleapis.com/css2?family=Arimo:ital,wght@0,400;0,700;1,700&display=swap">
<style>
  :root {
    --bg: #e4e5e7;
    --card: #ffffff;
    --brand-blue: #1f5fa8;
    --accent-blue: #2d7ac4;
    --ink: #3a3d42;
    --ink-soft: #5b5f66;
    --rule: #c9ccd1;
    --orange: #f08a1c;
  }
  * { box-sizing: border-box; margin: 0; padding: 0; }
  html, body { width: 1200px; height: 901px; overflow: hidden; }
  body {
    background: var(--bg);
    font-family: "Arimo", Arial, sans-serif;
    color: var(--ink);
    display: flex;
    align-items: center;
    justify-content: center;
    gap: 48px;
  }
  .card {
    width: 540px;
    height: 309px;
    background: var(--card);
    box-shadow: 0 6px 18px rgba(0,0,0,.18);
    position: relative;
    overflow: hidden;
  }
  .brand {
    display: flex;
    align-items: center;
    gap: 10px;
  }
  .brand-mark {
    width: 22px; height: 22px;
    background: var(--brand-blue);
    flex: none;
  }
  .brand-name {
    font-weight: 700;
    color: var(--brand-blue);
    font-size: 19px;
    letter-spacing: .5px;
    text-transform: uppercase;
    line-height: 1.1;
  }

  /* Front */
  .card-front .brand { position: absolute; left: 40px; top: 92px; width: 230px; }
  .card-front .rule {
    position: absolute; left: 0; top: 168px; width: 300px; height: 1px;
    background: var(--rule);
  }
  .contact {
    position: absolute; left: 300px; top: 150px; width: 230px;
  }
  .contact-name { color: var(--accent-blue); font-size: 15px; font-weight: 700; }
  .contact-title { font-size: 12px; color: var(--ink-soft); margin-top: 2px; }
  .contact-address { font-size: 12px; margin-top: 12px; line-height: 1.35; }
  .contact-lines { list-style: none; margin-top: 10px; }
  .contact-lines li {
    display: flex; align-items: center; gap: 7px;
    font-size: 12px; line-height: 17px; white-space: nowrap;
  }
  .contact-lines svg { width: 11px; height: 11px; flex: none; fill: var(--ink-soft); }

  /* Back */
  .card-back .brand { position: absolute; left: 40px; top: 40px; }
  .tagline {
    position: absolute; left: 40px; top: 112px;
    font-style: italic; font-weight: 700; font-size: 17px;
    color: var(--accent-blue);
  }
  .tagline-bar {
    position: absolute; left: 40px; top: 140px; width: 60px; height: 3px;
    background: var(--orange);
  }
  .services {
    position: absolute; left: 40px; top: 160px; right: 40px;
    display: grid; grid-template-columns: 1fr 1fr; column-gap: 24px;
    list-style: none;
  }
  .services li { font-size: 11.5px; line-height: 19px; color: var(--ink); }
</style>
</head>
<body>

<section class="card card-front" aria-label="Card front">
  <div class="brand">
    <span class="brand-mark"></span>
    <span class="brand-name">Brovalco Upkeep LLC</span>
  </div>
  <div class="rule"></div>
  <div class="contact">
    <p class="contact-name">Darrel Wickham</p>
    <p class="contact-title">President &amp; CEO</p>
    <p class="contact-address">2847 Tallow Bend Rd<br>Norristown PA 19403</p>
    <ul class="contact-lines">
      <li><svg viewBox="0 0 16 16"><path d="M3 1h3l1.5 4-2 1.2a9 9 0 0 0 4.3 4.3L11 8.5l4 1.5v3c0 1-1 2-2 2A12 12 0 0 1 1 3c0-1 1-2 2-2z"/></svg>610-555-0148</li>
      <li><svg viewBox="0 0 16 16"><path d="M4 0h8a1 1 0 0 1 1 1v14a1 1 0 0 1-1 1H4a1 1 0 0 1-1-1V1a1 1 0 0 1 1-1zm1 2v10h6V2zm3 11a1 1 0 1 0 0 2 1 1 0 0 0 0-2z"/></svg>610-555-0193</li>
      <li><svg viewBox="0 0 16 16"><path d="M1 3h14v10H1zm1.5 1.2V5l5.5 4 5.5-4v-.8L8 8z"/></svg>wwwdw@brovalco-example.com</li>
      <li><svg viewBox="0 0 16 16"><path d="M8 0a8 8 0 1 0 0 16A8 8 0 0 0 8 0zm0 1.5c.9 0 2 1.9 2.3 5.5H5.7C6 3.4 7.1 1.5 8 1.5zM1.6 7h2.6c.1-2 .5-3.6 1.1-4.7A6.5 6.5 0 0 0 1.6 7zm0 2a6.5 6.5 0 0 0 3.7 4.7C4.7 12.6 4.3 11 4.2 9zm4.1 0h4.6C10 12.6 8.9 14.5 8 14.5S6 12.6 5.7 9zm6.1 0c-.1 2-.5 3.6-1.1 4.7A6.5 6.5 0 0 0 14.4 9zm2.6-2a6.5 6.5 0 0 0-3.7-4.7c.6 1.1 1 2.7 1.1 4.7z"/></svg>www.brovalco-example.com</li>
    </ul>
  </div>
</section>

<section class="card card-back" aria-label="Card back">
  <div class="brand">
    <span class="brand-mark"></span>
    <span class="brand-name">Brovalco Upkeep LLC</span>
  </div>
  <p class="tagline">Professionally done for less than the rest</p>
  <div class="tagline-bar"></div>
  <ul class="services">
    <li>Commercial &amp; Residential</li>
    <li>Power washing services</li>
    <li>Interior &amp; Exterior</li>
    <li>Customized cleaning programs</li>
    <li>Window washing/Cleaning</li>
    <li>Fully licensed, insured,</li>
    <li>Green House, Skylight, Gutter</li>
    <li>and bonded professionals.</li>
  </ul>
</section>

</body>
</html>
```